Red Sea Boat trips in need of Business Card for Private Boat Tours

We need a Business card for a new business set-up in Egypt on the Red Sea for private snorkelling and boat excursions to one of the world's most beautiful reefs. We have wording logo already set-up which matches the boat but we need business cards to be bright and colourful with pictures of boat

Industry/Entity Type

Tourism

Contact Information for Business Card

Two Silver Gulls (font provided) Boat Trips

```html
<!DOCTYPE html>
<html lang="de">
<head>
<meta charset="utf-8">
<title>Two Silver Gulls – Visitenkarte</title>
<link rel="stylesheet" href="https://fonts.googleapis.com/css2?family=Roboto+Condensed:wght@400;500;700&display=swap">
<style>
  :root {
    --page-bg: #8c8c8c;
    --sky-top: #1d5cc8;
    --sky-low: #5b9be4;
    --shore: #d8a89a;
    --sea-light: #2ab4c6;
    --sea-deep: #0f7f97;
    --hull: #eef0f2;
    --canopy: #26326a;
    --reef-warm: #6b4a35;
    --reef-top: #1d4770;
    --reef-mid: #123154;
    --reef-bottom: #000000;
    --wordmark: #121417;
    --name-blue: #5a7fd0;
    --rule-blue: #5d82d4;
    --text-light: #f2f2f2;
    --icon-blue: #9fb4e6;
  }
  html, body {
    margin: 0;
    padding: 0;
    width: 1200px;
    height: 900px;
    overflow: hidden;
    background: var(--page-bg);
    font-family: "Roboto Condensed", "Arial Narrow", sans-serif;
  }
  .canvas {
    position: relative;
    width: 1200px;
    height: 900px;
  }
  .card {
    position: absolute;
    top: 151px;
    width: 386px;
    height: 599px;
    border-radius: 22px;
    overflow: hidden;
  }
  .card--front { left: 199px; }
  .card--back { left: 636px; }

  .front-photo {
    position: absolute;
    inset: 0;
    background:
      radial-gradient(ellipse 55% 12% at 62% 57%, rgba(38,50,106,0.85) 0%, rgba(38,50,106,0) 100%),
      radial-gradient(ellipse 75% 45% at 72% 78%, rgba(238,240,242,0.95) 0%, rgba(238,240,242,0.6) 55%, rgba(238,240,242,0) 100%),
      radial-gradient(ellipse 45% 8% at 68% 40%, rgba(216,168,154,0.9) 0%, rgba(216,168,154,0) 100%),
      linear-gradient(180deg,
        var(--sky-top) 0%,
        var(--sky-low) 30%,
        #cfc3b0 40%,
        var(--sea-light) 48%,
        #23a2b8 70%,
        var(--sea-deep) 100%);
  }
  .wordmark {
    position: absolute;
    top: 60px;
    left: 0;
    right: 0;
    margin: 0;
    text-align: center;
    font-size: 46px;
    font-weight: 700;
    color: var(--wordmark);
    letter-spacing: 0.3px;
  }

  .back-photo {
    position: absolute;
    inset: 0;
    background:
      radial-gradient(ellipse 42% 36% at 22% 30%, rgba(107,74,53,0.85) 0%, rgba(107,74,53,0.35) 60%, rgba(107,74,53,0) 100%),
      linear-gradient(180deg,
        var(--reef-top) 0%,
        var(--reef-mid) 45%,
        #08182a 68%,
        var(--reef-bottom) 85%);
  }
  .contact {
    position: absolute;
    left: 33px;
    top: 344px;
    right: 20px;
    color: var(--text-light);
  }
  .contact__name {
    margin: 0;
    font-size: 33px;
    font-weight: 700;
    color: var(--name-blue);
    line-height: 1;
  }
  .contact__role {
    margin: 8px 0 0;
    font-size: 16.5px;
    font-weight: 400;
    letter-spacing: 0.3px;
  }
  .contact__rule {
    width: 254px;
    height: 1px;
    background: var(--rule-blue);
    margin: 16px 0 18px;
  }
  .contact__list {
    list-style: none;
    margin: 0;
    padding: 0;
    font-size: 16.5px;
    font-weight: 400;
    letter-spacing: 0.4px;
  }
  .contact__item {
    display: flex;
    align-items: flex-start;
    gap: 6px;
    line-height: 26px;
  }
  .contact__item--address { margin-bottom: 12px; }
  .contact__item--phone { letter-spacing: 2px; }
  .contact__icon {
    width: 12px;
    height: 12px;
    margin-top: 7px;
    flex: none;
  }
</style>
</head>
<body>
<main class="canvas">
  <section class="card card--front">
    <div class="front-photo" role="img" aria-label="Foto eines weißen Motorboots mit blauem Sonnendach im türkisen Hafenwasser vor rosa Häusern und Palmen am Ufer"></div>
    <h1 class="wordmark">Two Silver Gulls</h1>
  </section>

  <section class="card card--back">
    <div class="back-photo" role="img" aria-label="Unterwasserfoto eines Korallenriffs mit roten Fischschwärmen und einem Taucher im blauen Wasser"></div>
    <div class="contact">
      <h2 class="contact__name">Jonas Keller</h2>
      <p class="contact__role">Geschäftsführender/Gesellschafter</p>
      <div class="contact__rule"></div>
      <ul class="contact__list">
        <li class="contact__item contact__item--address">
          <svg class="contact__icon" viewBox="0 0 12 12" aria-hidden="true"><path d="M6 0.5a4 4 0 0 0-4 4c0 3 4 7 4 7s4-4 4-7a4 4 0 0 0-4-4z" fill="var(--icon-blue)"/><circle cx="6" cy="4.5" r="1.5" fill="#000"/></svg>
          <span>Lindenweg 12<br>10115 Berlin</span>
        </li>
        <li class="contact__item contact__item--phone">
          <svg class="contact__icon" viewBox="0 0 12 12" aria-hidden="true"><path d="M2.5 1l2 2.2-1 1.3c.7 1.5 1.8 2.6 3.3 3.3l1.3-1 2.2 2-1.2 1.7C5.5 10.3 1.7 6.5 0.8 2.2z" fill="var(--icon-blue)"/></svg>
          <span>+49 170 5550142</span>
        </li>
        <li class="contact__item">
          <svg class="contact__icon" viewBox="0 0 12 12" aria-hidden="true"><rect x="0.5" y="2.5" width="11" height="7.5" fill="var(--icon-blue)"/><path d="M0.5 2.5l5.5 4 5.5-4" fill="none" stroke="#000" stroke-width="1"/></svg>
          <span>j.keller@seaviewtrips.de</span>
        </li>
        <li class="contact__item">
          <svg class="contact__icon" viewBox="0 0 12 12" aria-hidden="true"><g fill="none" stroke="var(--icon-blue)" stroke-width="1"><circle cx="6" cy="6" r="5"/><ellipse cx="6" cy="6" rx="2.2" ry="5"/><path d="M1 6h10M2 3.3h8M2 8.7h8"/></g></svg>
          <span>www.seaviewtrips.de</span>
        </li>
      </ul>
    </div>
  </section>
</main>
</body>
</html>
```